Business Card Design Project - ol taviran group

dear Sirs

we need business card design for our group ( OL Taviran Group ) , i have got the Logo design of our group from pixel forum in previous , so all need details relating to our group i think available with you, as well as the the chosen logo design

we hope to provide us with business card logo that to be appropaite and satisfactory to us .

thanks

note : logo design of our group is attached .

Reason: please extend the deadline of my project for additional 15 days because i didn't received appropriate design for our gruop yet . kindly beaware that i have received 77 design till now , supossed to send me 200-250 design at least . thanks

contents

name : Selim OR Haddani

position : Operation Manager

• person name

group logo
• logo color matching with back background

```html
<!DOCTYPE html>
<html lang="en">
<head>
<meta charset="utf-8">
<title>OL Taviran Group — Business Card</title>
<link rel="stylesheet" href="https://fonts.googleapis.com/css2?family=Source+Sans+3:wght@400;600;700&display=swap">
<style>
  :root {
    --page: #ffffff;
    --card-light: #ffffff;
    --card-dark: #060606;
    --brand-blue: #0b4f8e;
    --name-blue: #1d4f8a;
    --gold: #c9a043;
    --ink: #4a4a4a;
    --rule: #9a9a9a;
    --white: #ffffff;
  }
  * { box-sizing: border-box; margin: 0; padding: 0; }
  html, body {
    width: 1200px; height: 900px; overflow: hidden;
    background: var(--page);
    font-family: "Source Sans 3", "Myriad Pro", Arial, sans-serif;
  }
  .stage { position: relative; width: 1200px; height: 900px; }
  .card {
    position: absolute; left: 305px; width: 628px; height: 359px;
    overflow: hidden;
    box-shadow: 6px 8px 10px rgba(0,0,0,0.35);
  }
  .card--front { top: 57px; background: var(--card-light); }
  .card--back { top: 471px; background: var(--card-dark); }
  .card__wave { position: absolute; inset: 0; width: 628px; height: 359px; }
  .card__web {
    position: absolute; left: 0; right: 0; top: 320px;
    text-align: center; color: var(--white);
    font-size: 19px; font-weight: 400; letter-spacing: 0.2px;
  }
  .wordmark {
    position: absolute; color: var(--brand-blue);
    font-weight: 700; text-transform: uppercase; white-space: nowrap;
    letter-spacing: 0.5px; line-height: 1;
  }
  .card--front .wordmark { left: 44px; top: 62px; font-size: 38px; }
  .card--back .wordmark { left: 0; right: 0; top: 152px; text-align: center; font-size: 44px; }
  .person {
    position: absolute; right: 350px; top: 203px; text-align: right;
  }
  .person__name { color: var(--name-blue); font-size: 22px; font-weight: 700; line-height: 1.1; }
  .person__role { color: var(--ink); font-size: 15px; margin-top: 4px; }
  .divider {
    position: absolute; left: 315px; top: 172px; width: 1px; height: 124px;
    background: var(--rule);
  }
  .contact {
    position: absolute; left: 346px; top: 174px; list-style: none;
    color: var(--ink); font-size: 15px; line-height: 21.5px;
  }
  .contact__item { display: flex; align-items: center; height: 21.5px; }
  .contact__icon { width: 15px; height: 15px; margin-right: 8px; flex: none; }
  .contact__item--address { padding-left: 0; }
</style>
</head>
<body>
<main class="stage">

  <section class="card card--front" aria-label="Business card front">
    <svg class="card__wave" viewBox="0 0 628 359" aria-hidden="true">
      <path d="M0 276 Q314 347 628 281 L628 359 L0 359 Z" fill="var(--brand-blue)"/>
      <path d="M0 270 Q314 339 628 275 L628 279 Q314 347 0 275 Z" fill="var(--gold)"/>
    </svg>

    <div class="wordmark">OL Taviran Group</div>

    <div class="person">
      <div class="person__name">Selim OR Haddani</div>
      <div class="person__role">Operation Manager</div>
    </div>

    <div class="divider"></div>

    <ul class="contact">
      <li class="contact__item contact__item--address">P.O. Box 482, Eastwood, Vic, 3081</li>
      <li class="contact__item">
        <svg class="contact__icon" viewBox="0 0 16 16" aria-hidden="true"><circle cx="8" cy="8" r="8" fill="var(--brand-blue)"/><path d="M5 4.5 L6.6 4.2 L7.3 6.2 L6.3 7 Q7 8.8 8.9 9.7 L9.8 8.7 L11.8 9.4 L11.5 11 Q7.5 11.3 5 6.5 Z" fill="#fff"/></svg>
        02 5550 1482
      </li>
      <li class="contact__item">
        <svg class="contact__icon" viewBox="0 0 16 16" aria-hidden="true"><circle cx="8" cy="8" r="8" fill="var(--brand-blue)"/><rect x="4" y="7" width="8" height="4.5" fill="#fff"/><rect x="5.5" y="4" width="5" height="3" fill="#fff"/></svg>
        02 5550 1483
      </li>
      <li class="contact__item">
        <svg class="contact__icon" viewBox="0 0 16 16" aria-hidden="true"><circle cx="8" cy="8" r="8" fill="var(--brand-blue)"/><rect x="5.5" y="3.5" width="5" height="9" rx="1" fill="#fff"/><rect x="6.5" y="5" width="3" height="4" fill="var(--brand-blue)"/></svg>
        02 5550 1484
      </li>
      <li class="contact__item">
        <svg class="contact__icon" viewBox="0 0 16 16" aria-hidden="true"><circle cx="8" cy="8" r="8" fill="var(--brand-blue)"/><rect x="4" y="5" width="8" height="6" fill="#fff"/><path d="M4 5 L8 8.3 L12 5" fill="none" stroke="var(--brand-blue)" stroke-width="1"/></svg>
        selim@oltaviran.com
      </li>
    </ul>

    <div class="card__web">www.oltaviran.com</div>
  </section>

  <section class="card card--back" aria-label="Business card back">
    <svg class="card__wave" viewBox="0 0 628 359" aria-hidden="true">
      <path d="M0 276 Q314 347 628 281 L628 359 L0 359 Z" fill="var(--brand-blue)"/>
      <path d="M0 270 Q314 339 628 275 L628 279 Q314 347 0 275 Z" fill="var(--gold)"/>
    </svg>

    <div class="wordmark">OL Taviran Group</div>

    <div class="card__web">www.oltaviran.com</div>
  </section>

</main>
</body>
</html>
```